Life Coach for Lawyers Business Card Design

Elegant, original, business card design for life coaching service for associate attorneys who work in big law and struggle with stress, overwhelm, and time management. Double sided design.

Target Market(s)

Women associate attorneys who work in big law and struggle with stress, overwhelm, and time management.

Industry/Entity Type

Life Coaching

Contact Information for Business Card

Marissa Pendrell
Life Coach
518.677.3941
calmbriefcounsel.net
marissa@calmbriefcounsel.net
@calmbriefcounsel (Instagram)

Font styles to use
Other font styles liked:
• Silver South font duo. See uploaded files.

Requirements
Must have
• Icons for phone, website, email, and Instagram instead of words. Specific colors used in my logo (171B2B, 421121, FFFFFF)
Nice to have
• Foil. Embossed. Feminine design.
Should not have
• Any colors other than those used in logo. See uploaded files.

```html
<!DOCTYPE html>
<html lang="en">
<head>
<meta charset="utf-8">
<title>Calm Brief Counsel — Business Card</title>
<link rel="stylesheet" href="https://fonts.googleapis.com/css2?family=Playfair+Display:wght@400;700;800&display=swap">
<style>
  :root {
    --ink: #171B2B;
    --wine: #421121;
    --paper: #FFFFFF;
    --page: #FFFFFF;
    --shadow: rgba(0, 0, 0, 0.28);
  }
  * { box-sizing: border-box; margin: 0; padding: 0; }
  html, body {
    width: 1200px;
    height: 1200px;
    overflow: hidden;
    background: var(--page);
    font-family: "Playfair Display", Georgia, serif;
  }
  .stage { position: relative; width: 1200px; height: 1200px; }

  .card {
    position: absolute;
    left: 183px;
    width: 835px;
    height: 500px;
    box-shadow: 0 4px 14px var(--shadow);
  }

  /* Front */
  .card-front { top: 66px; background: var(--wine); color: var(--paper); }
  .brand-seal {
    position: absolute;
    left: 269px; top: 92px;
    width: 296px; height: 296px;
    border: 1.5px solid var(--paper);
    border-radius: 50%;
    display: flex; align-items: center; justify-content: center;
    text-align: center;
  }
  .brand-seal .brand-name {
    font-size: 34px;
    font-weight: 400;
    line-height: 1.2;
    color: var(--paper);
  }
  .front-url {
    position: absolute;
    left: 0; right: 0; top: 422px;
    text-align: center;
    font-size: 23px;
    letter-spacing: 0.2px;
  }
  .front-url strong { font-weight: 700; }

  /* Back */
  .card-back { top: 622px; background: var(--paper); }
  .back-brand {
    position: absolute;
    left: 56px; top: 92px;
    font-size: 40px;
    font-weight: 700;
    color: var(--wine);
    line-height: 1;
  }
  .person { position: absolute; left: 56px; top: 250px; }
  .person-name {
    font-size: 35px;
    font-weight: 800;
    color: var(--ink);
    line-height: 1.1;
  }
  .person-role {
    font-size: 22px;
    letter-spacing: 5px;
    color: var(--wine);
    margin-top: 2px;
  }
  .contact-list {
    position: absolute;
    left: 58px; top: 346px;
    list-style: none;
  }
  .contact-item {
    display: flex; align-items: center;
    height: 37px;
    font-size: 23px;
    color: var(--ink);
  }
  .contact-icon { width: 22px; height: 22px; margin-right: 22px; flex: none; }
  .contact-icon * { fill: none; stroke: var(--wine); stroke-width: 2; }
</style>
</head>
<body>
<main class="stage">
  <section class="card card-front" aria-label="Card front">
    <div class="brand-seal">
      <span class="brand-name">Calm Brief<br>Counsel</span>
    </div>
    <p class="front-url">www.<strong>calmbriefcounsel</strong>.net</p>
  </section>

  <section class="card card-back" aria-label="Card back">
    <div class="back-brand">Calm Brief Counsel</div>
    <div class="person">
      <h1 class="person-name">Marissa Pendrell</h1>
      <p class="person-role">LIFE COACH</p>
    </div>
    <ul class="contact-list">
      <li class="contact-item">
        <svg class="contact-icon" viewBox="0 0 22 22" aria-hidden="true">
          <rect x="5" y="1" width="12" height="20" rx="2"/>
          <line x1="9" y1="17" x2="13" y2="17"/>
        </svg>
        518.677.3941
      </li>
      <li class="contact-item">
        <svg class="contact-icon" viewBox="0 0 22 22" aria-hidden="true">
          <path d="M2 9 L11 3 L20 9 V19 H2 Z"/>
          <path d="M2 9 L11 15 L20 9"/>
        </svg>
        marissa@calmbriefcounsel.net
      </li>
      <li class="contact-item">
        <svg class="contact-icon" viewBox="0 0 22 22" aria-hidden="true">
          <rect x="2" y="2" width="18" height="18" rx="4"/>
        </svg>
        @calmbriefcounsel
      </li>
    </ul>
  </section>
</main>
</body>
</html>
```